Varden Hub, LLC. is the name of the company that will be an Internet startup working in E-commerce and

We are a new company and going to start the business by hiring people we need. We are on “Hiring Now…” status right now which we like to be displayed on the website homepage.
The website should allow us to start the hiring process with letting people see and apply for jobs posted on the website.

the company logo is attached.

Target Market(s)

Tech Job Seekers, Programmers, iOS and Android Developers, Software engineers, Graphic designers, QA engineers, Customer Service Reps,...

Industry/Entity Type

Internet

Number of Pages Required

5+ page

Font styles to use
Serif
Sans Serif

Colors

Designer to choose colors to be used in the design.

Requirements
Must have
• We need a system to help job seekers to upload the resume and cover letter and fill the required forms and answer some questions on a form designed to evaluate the job seekers and let them know if they fit in the position and should apply for it.
• We also want job seekers to do a Pre-Employment Tests including Aptitude, Personality, and Skills after they qualified for a job which links our website to web-based pre-employment testing services websites like (Metrica, Talvex, Brunholt & Partners, Dovin Evaluation, …)

```html
<!DOCTYPE html>
<html lang="en">
<head>
<meta charset="utf-8">
<title>Varden Hub – Join the Best Job Finder</title>
<link href="https://fonts.googleapis.com/css2?family=Montserrat:wght@400;600;700;800&family=Open+Sans:wght@400;600;700&display=swap" rel="stylesheet">
<style>
:root{
  --teal:#3ba7c6;
  --teal-dark:#2d8eab;
  --orange:#f08a3e;
  --ink:#3b4350;
  --text:#6b7380;
  --muted:#9aa1ab;
  --line:#d9dde2;
  --band:#eeeff1;
  --dark:#3c4452;
  --darker:#2f3641;
  --white:#ffffff;
}
*{box-sizing:border-box;margin:0;padding:0}
html,body{width:1200px;height:4072px;overflow:hidden}
body{font-family:"Open Sans",Arial,sans-serif;color:var(--text);background:var(--white);font-size:14px}
h1,h2,h3,.nav a,.btn{font-family:"Montserrat",Arial,sans-serif}
.wrap{width:1010px;margin:0 auto;position:relative}

/* top bar */
.topbar{height:40px;background:var(--dark)}
.topbar .wrap{display:flex;align-items:center;justify-content:space-between;height:40px;width:1100px}
.topsearch{width:150px;height:24px;background:#fff;border-radius:2px;font-size:10px;color:var(--muted);padding:5px 8px}
.toplinks{display:flex;align-items:center;gap:20px;font-size:10px;font-weight:700;color:#fff;letter-spacing:.5px}
.btn-small{background:var(--teal);color:#fff;padding:6px 14px;border-radius:2px;font-size:10px}

/* nav */
.nav{height:100px}
.nav .wrap{display:flex;align-items:center;justify-content:space-between;height:100px;width:1100px}
.brand{display:flex;align-items:center;gap:10px;font-family:"Montserrat",sans-serif;font-weight:800;font-size:28px;color:var(--teal)}
.brand i{width:16px;height:16px;border-radius:50%;background:var(--orange);display:block}
.menu{display:flex;gap:28px}
.menu a{font-size:12px;font-weight:600;color:var(--ink);text-decoration:none;letter-spacing:.6px}
.menu a.active{color:var(--orange)}

/* hero */
.hero{height:690px;position:relative;background:linear-gradient(100deg,#4f8f9f 0%,#6fb0bf 45%,#9fcfd8 100%)}
.hero-photo{position:absolute;inset:0}
.hero .wrap{width:1100px;padding-top:180px}
.hero h1{color:#fff;font-size:58px;line-height:64px;font-weight:800;letter-spacing:1px}
.hero-search{display:flex;gap:16px;margin-top:110px}
.select{width:220px;height:40px;background:#fff;border-radius:2px;font-size:12px;color:var(--muted);padding:11px 14px;position:relative}
.select:after{content:"";position:absolute;right:14px;top:16px;border:5px solid transparent;border-top-color:var(--muted)}
.btn{background:var(--teal);color:#fff;font-weight:700;font-size:12px;letter-spacing:.6px;border-radius:2px;display:inline-block;text-align:center}
.hero-search .btn{width:150px;height:40px;line-height:40px}

/* section heads */
.sec-title{text-align:center;font-size:24px;font-weight:600;color:var(--ink);letter-spacing:1.5px}
.sec-title:after{content:"";display:block;width:60px;height:3px;background:var(--orange);margin:12px auto 0}

/* how it works */
.how{height:300px;padding-top:92px}
.steps{position:relative;display:flex;justify-content:space-between;width:640px;margin:48px auto 0}
.steps:before{content:"";position:absolute;left:-60px;right:-60px;top:18px;height:1px;background:var(--line)}
.step{width:180px;text-align:center;position:relative}
.step .num{width:38px;height:38px;border:2px solid var(--teal);border-radius:50%;background:#fff;margin:0 auto;font-size:15px;color:var(--teal);line-height:34px}
.step h3{font-size:13px;font-weight:600;color:var(--ink);margin:16px 0 8px;letter-spacing:.5px}
.step p{font-size:11px;line-height:17px;color:var(--muted)}

/* categories */
.cats{height:420px;padding-top:32px}
.cat-grid{display:grid;grid-template-columns:repeat(3,330px);gap:10px 10px;justify-content:space-between;margin-top:40px}
.cat{height:82px;border:2px solid var(--line);border-radius:3px;display:flex;align-items:center;justify-content:center;gap:14px;font-size:14px;color:var(--ink)}
.cat svg{width:26px;height:26px;stroke:var(--teal);fill:none;stroke-width:2}
.show-more{text-align:center;margin-top:34px;font-family:"Montserrat",sans-serif;font-size:12px;font-weight:700;color:var(--ink);letter-spacing:.6px}
.show-more:after{content:"";display:block;width:40px;height:2px;background:var(--orange);margin:6px auto 0}

/* testimonials */
.testimonials{height:290px;background:var(--band);margin-top:88px;padding-top:48px;position:relative}
.testimonials .quote{width:720px;margin:28px auto 0;text-align:center;font-size:14px;line-height:24px;color:var(--ink)}
.stars{text-align:center;margin-top:16px;color:var(--orange);font-size:14px;letter-spacing:2px}
.author{text-align:center;font-size:11px;color:var(--teal);letter-spacing:1.5px;margin-top:6px}
.arrow{position:absolute;top:140px;width:18px;height:18px;border-left:3px solid #c4c8ce;border-bottom:3px solid #c4c8ce}
.arrow.prev{left:100px;transform:rotate(45deg)}
.arrow.next{right:100px;transform:rotate(-135deg)}

/* jobs */
.jobs{height:1000px;padding-top:104px}
.jobs .lead{text-align:center;font-size:12px;color:var(--muted);margin-top:22px}
.jobs .count{text-align:center;font-size:24px;color:var(--teal);margin-top:24px}
.filter{display:flex;gap:10px;align-items:center;background:var(--band);height:52px;padding:0 14px;margin-top:28px}
.filter .select{width:230px;height:30px;padding:7px 12px;font-size:11px}
.filter .select:after{top:12px}
.filter .btn{width:140px;height:30px;line-height:30px;margin-left:auto}
.job-list{margin-top:16px}
.job{display:flex;align-items:center;height:77px;border-bottom:1px solid var(--line);font-size:12px}
.job .logo{width:46px;height:46px;border:1px solid var(--line);border-radius:3px;background:#f4f5f6;margin:0 18px 0 8px}
.job .role{width:225px;line-height:18px;color:var(--ink)}
.job .role span{display:block;color:var(--orange);font-size:11px}
.job .meta{display:flex;align-items:center;gap:10px;width:180px;color:var(--text)}
.job .meta svg{width:16px;height:16px;stroke:var(--orange);fill:none;stroke-width:2}
.job .meta.pay{width:170px}
.job .more{color:var(--teal);font-size:11px;margin-left:auto;display:flex;align-items:center;gap:10px;padding-right:10px}
.job .more:after{content:"›";font-size:18px;color:var(--muted)}
.jobs .cta{text-align:center;margin-top:54px}
.jobs .cta .btn{width:170px;height:38px;line-height:38px;font-weight:600}

/* milestones */
.milestones{height:365px;background:var(--dark);padding-top:58px;color:#fff}
.milestones h2{text-align:center;font-size:24px;font-weight:600;letter-spacing:1.5px}
.milestones p{text-align:center;font-size:12px;margin-top:18px;color:#e4e7eb}
.stats{display:flex;justify-content:center;gap:38px;margin-top:44px}
.stat{width:234px;height:120px;border:1px solid #8a93a0;text-align:center;padding-top:28px}
.stat small{display:block;font-size:14px;color:#e4e7eb}
.stat strong{display:block;font-family:"Montserrat",sans-serif;font-size:26px;font-weight:600;margin-top:10px}

/* partners */
.partners{height:140px;display:flex;align-items:center;justify-content:center;gap:90px}
.partners span{font-family:"Open Sans",sans-serif;font-weight:700;font-size:28px;color:#b7c6d8}

/* footer */
.footer{height:372px;background:var(--darker);text-align:center;color:#fff;padding-top:110px}
.footer-links{display:flex;justify-content:center;gap:18px;font-size:13px;color:#e6e8eb}
.footer-links b{color:var(--muted);font-weight:400}
.follow{margin-top:46px;font-size:14px;font-weight:700}
.socials{display:flex;justify-content:center;gap:14px;margin-top:18px}
.socials i{width:32px;height:32px;border:1px solid #8a93a0;border-radius:50%;display:block}
.copy{margin-top:56px;font-size:11px;color:var(--muted)}
</style>
</head>
<body>

<header class="topbar">
  <div class="wrap">
    <div class="topsearch">Search site</div>
    <div class="toplinks"><span>SIGN IN</span><span>LOGIN IN</span><span class="btn-small">POST A JOB</span></div>
  </div>
</header>

<nav class="nav">
  <div class="wrap">
    <div class="brand"><i></i>Varden Hub</div>
    <div class="menu">
      <a href="#">HOME</a><a href="#">RESUME HELP</a><a href="#" class="active">EDUCATION</a><a href="#">MARKET RESEARCH</a><a href="#">WORK AT HOME</a>
    </div>
  </div>
</nav>

<section class="hero">
  <div class="hero-photo" role="img" aria-label="Photo of a relaxed job seeker stretching at a desk with a laptop in a bright office"></div>
  <div class="wrap">
    <h1>JOIN THE BEST<br>JOB FINDER</h1>
    <div class="hero-search">
      <div class="select">Job Title...</div>
      <div class="select">City, State...</div>
      <div class="btn">FIND JOBS</div>
    </div>
  </div>
</section>

<section class="how">
  <h2 class="sec-title">HOW JOBVANE WORKS</h2>
  <div class="steps">
    <div class="step"><div class="num">1</div><h3>CREATE AN ACCOUNT</h3><p>Sign up in minutes, add your details and set the roles and places you want to work in.</p></div>
    <div class="step"><div class="num">2</div><h3>SEARCH DESIRED JOB</h3><p>Browse open roles by title, city and category, then save the jobs that fit your skills.</p></div>
    <div class="step"><div class="num">3</div><h3>SEND YOUR RESUME</h3><p>Upload your resume and cover letter, answer a few questions and apply in one click.</p></div>
  </div>
</section>

<section class="cats">
  <div class="wrap">
    <h2 class="sec-title">POPULAR JOB SEARCH</h2>
    <div class="cat-grid">
      <div class="cat"><svg viewBox="0 0 24 24"><path d="M4 20l4-1 11-11-3-3L5 16z"/></svg>Design, Art &amp; Multimedia</div>
      <div class="cat"><svg viewBox="0 0 24 24"><rect x="7" y="2" width="10" height="20" rx="2"/><path d="M11 18h2"/></svg>Mobile Developer</div>
      <div class="cat"><svg viewBox="0 0 24 24"><path d="M8 3L3 7l3 3 2-1v12h8V9l2 1 3-3-5-4c-1 2-5 2-8 0z"/></svg>Fashion</div>
      <div class="cat"><svg viewBox="0 0 24 24"><path d="M3 10v4h4l8 5V5L7 10z"/><path d="M18 9c2 2 2 4 0 6"/></svg>Sales &amp; Marketing</div>
      <div class="cat"><svg viewBox="0 0 24 24"><rect x="3" y="4" width="18" height="12" rx="1"/><path d="M9 20h6M12 16v4M9 9l-2 2 2 2M15 9l2 2-2 2"/></svg>Web Developer</div>
      <div class="cat"><svg viewBox="0 0 24 24"><path d="M12 3v18M7 6h10M5 10h14"/><circle cx="12" cy="15" r="2"/></svg>Medicine</div>
      <div class="cat"><svg viewBox="0 0 24 24"><path d="M3 21h18M6 21V12M11 21V7M16 21v-6M20 21V4"/></svg>Accounting / Finance</div>
      <div class="cat"><svg viewBox="0 0 24 24"><circle cx="12" cy="7" r="4"/><path d="M4 21c1-5 4-7 8-7s7 2 8 7z"/></svg>Administration</div>
      <div class="cat"><svg viewBox="0 0 24 24"><path d="M3 5h7c1 0 2 1 2 2v13c0-1-1-2-2-2H3zM21 5h-7c-1 0-2 1-2 2v13c0-1 1-2 2-2h7z"/></svg>Education</div>
    </div>
    <div class="show-more">SHOW MORE</div>
  </div>
</section>

<section class="testimonials">
  <h2 class="sec-title">TESTIMONIALS</h2>
  <p class="quote">Lorem ipsum dolor sit amet, consectetur adipiscing elit. Etiam aliquam sed enim id sodales. Phasellus consequat arcu eu placerat euismod. Nullam convallis ac orci non volutpat volutpat.</p>
  <div class="stars">★★★</div>
  <div class="author">DARIN HOLLOWAY</div>
  <span class="arrow prev"></span><span class="arrow next"></span>
</section>

<section class="jobs">
  <div class="wrap">
    <h2 class="sec-title">LATEST JOB OPENINGS</h2>
    <p class="lead">Make the most of the opportunity available by browsing among the most trending categories and get hired today.</p>
    <p class="count">We found 8,039,827 matches jobs, you are watching 8 to 97</p>
    <div class="filter">
      <div class="select">Select Category</div>
      <div class="select">Search by city</div>
      <div class="select">Full Time</div>
      <div class="btn">SEARCH JOB</div>
    </div>
    <div class="job-list">
      <div class="job"><div class="logo"></div><div class="role">Web Developer<span>jobmail.com</span></div><div class="meta"><svg viewBox="0 0 24 24"><path d="M12 22s7-7 7-12a7 7 0 0 0-14 0c0 5 7 12 7 12z"/><circle cx="12" cy="10" r="2"/></svg>San Francisco</div><div class="meta"><svg viewBox="0 0 24 24"><circle cx="12" cy="12" r="9"/><path d="M12 7v5l3 2"/></svg>Part Time</div><div class="meta pay"><svg viewBox="0 0 24 24"><rect x="3" y="3" width="18" height="18" rx="2"/><path d="M12 6v12M15 9h-4a2 2 0 0 0 0 4h2a2 2 0 0 1 0 4H9"/></svg>$700</div><div class="more">Learn more about the work</div></div>
      <div class="job"><div class="logo"></div><div class="role">Marketing Affiliate<span>jobmail.com</span></div><div class="meta"><svg viewBox="0 0 24 24"><path d="M12 22s7-7 7-12a7 7 0 0 0-14 0c0 5 7 12 7 12z"/><circle cx="12" cy="10" r="2"/></svg>Monaco</div><div class="meta"><svg viewBox="0 0 24 24"><circle cx="12" cy="12" r="9"/><path d="M12 7v5l3 2"/></svg>Full Time</div><div class="meta pay"><svg viewBox="0 0 24 24"><rect x="3" y="3" width="18" height="18" rx="2"/><path d="M12 6v12M15 9h-4a2 2 0 0 0 0 4h2a2 2 0 0 1 0 4H9"/></svg>$5,000</div><div class="more">Learn more about the work</div></div>
      <div class="job"><div class="logo"></div><div class="role">Web Designer<span>jobmail.com</span></div><div class="meta"><svg viewBox="0 0 24 24"><path d="M12 22s7-7 7-12a7 7 0 0 0-14 0c0 5 7 12 7 12z"/><circle cx="12" cy="10" r="2"/></svg>London</div><div class="meta"><svg viewBox="0 0 24 24"><circle cx="12" cy="12" r="9"/><path d="M12 7v5l3 2"/></svg>Internship</div><div class="meta pay"><svg viewBox="0 0 24 24"><rect x="3" y="3" width="18" height="18" rx="2"/><path d="M12 6v12M15 9h-4a2 2 0 0 0 0 4h2a2 2 0 0 1 0 4H9"/></svg>$1,200</div><div class="more">Learn more about the work</div></div>
      <div class="job"><div class="logo"></div><div class="role">Web Developer<span>jobmail.com</span></div><div class="meta"><svg viewBox="0 0 24 24"><path d="M12 22s7-7 7-12a7 7 0 0 0-14 0c0 5 7 12 7 12z"/><circle cx="12" cy="10" r="2"/></svg>San Francisco</div><div class="meta"><svg viewBox="0 0 24 24"><circle cx="12" cy="12" r="9"/><path d="M12 7v5l3 2"/></svg>Part Time</div><div class="meta pay"><svg viewBox="0 0 24 24"><rect x="3" y="3" width="18" height="18" rx="2"/><path d="M12 6v12M15 9h-4a2 2 0 0 0 0 4h2a2 2 0 0 1 0 4H9"/></svg>$700</div><div class="more">Learn more about the work</div></div>
      <div class="job"><div class="logo"></div><div class="role">Marketing Affiliate<span>jobmail.com</span></div><div class="meta"><svg viewBox="0 0 24 24"><path d="M12 22s7-7 7-12a7 7 0 0 0-14 0c0 5 7 12 7 12z"/><circle cx="12" cy="10" r="2"/></svg>Monaco</div><div class="meta"><svg viewBox="0 0 24 24"><circle cx="12" cy="12" r="9"/><path d="M12 7v5l3 2"/></svg>Full Time</div><div class="meta pay"><svg viewBox="0 0 24 24"><rect x="3" y="3" width="18" height="18" rx="2"/><path d="M12 6v12M15 9h-4a2 2 0 0 0 0 4h2a2 2 0 0 1 0 4H9"/></svg>$5,000</div><div class="more">Learn more about the work</div></div>
      <div class="job"><div class="logo"></div><div class="role">Web Designer<span>jobmail.com</span></div><div class="meta"><svg viewBox="0 0 24 24"><path d="M12 22s7-7 7-12a7 7 0 0 0-14 0c0 5 7 12 7 12z"/><circle cx="12" cy="10" r="2"/></svg>London</div><div class="meta"><svg viewBox="0 0 24 24"><circle cx="12" cy="12" r="9"/><path d="M12 7v5l3 2"/></svg>Internship</div><div class="meta pay"><svg viewBox="0 0 24 24"><rect x="3" y="3" width="18" height="18" rx="2"/><path d="M12 6v12M15 9h-4a2 2 0 0 0 0 4h2a2 2 0 0 1 0 4H9"/></svg>$1,200</div><div class="more">Learn more about the work</div></div>
    </div>
    <div class="cta"><span class="btn">Learn more Jobs</span></div>
  </div>
</section>

<section class="milestones">
  <h2>OUR SUCCESSFUL MILESTONES</h2>
  <p>Lorem ipsum dolor sit amet, consectetur adipiscing elit. Etiam aliquam sed enim id sodales, lorem ipsum sodales arcu.</p>
  <div class="stats">
    <div class="stat"><small>Jobs Posted</small><strong>8,039,827</strong></div>
    <div class="stat"><small>Companies Registered</small><strong>4329</strong></div>
    <div class="stat"><small>Candidate Profiles</small><strong>73982</strong></div>
  </div>
</section>

<section class="partners">
  <span>Castline</span><span>Paywell</span><span>Microdyne</span><span>Nettora</span><span>Fortwell</span>
</section>

<footer class="footer">
  <div class="footer-links"><span>Home</span><b>•</b><span>Resume Help</span><b>•</b><span>Education</span><b>•</b><span>Market Research</span><b>•</b><span>Work at Home</span></div>
  <div class="follow">Follow us</div>
  <div class="socials"><i></i><i></i><i></i></div>
  <div class="copy">Copyright © 2017 Varden Hub, LLC. Privacy Policy · Terms of Use · Advertising · Affiliates</div>
</footer>

</body>
</html>
```